Need a new letterhead

Need a new fresh exciting letterhead. Remove the footer...info is outdated.

Target Market(s)

B2B

Industry/Entity Type

Electrical Power

Colors

Designer to choose colors to be used in the design.

Requirements
Must have
• Red and Blue Brindlecroft Arcwell Logo
Nice to have
• Lighting the way to sustainability in footer...reorganize the words?

```html
<!DOCTYPE html>
<html lang="en">
<head>
<meta charset="utf-8">
<title>Brindlecroft Arcwell Letterhead</title>
<link href="https://fonts.googleapis.com/css2?family=Archivo:wght@800&family=Lato:wght@400&display=swap" rel="stylesheet">
<style>
  :root {
    --brand-red: #ec2027;
    --brand-blue: #2b3990;
    --paper: #fefefe;
  }
  html, body {
    margin: 0;
    padding: 0;
    overflow: hidden;
    background: var(--paper);
  }
  .letterhead {
    position: relative;
    width: 933px;
    height: 1200px;
    background: var(--paper);
    overflow: hidden;
  }
  .brand-block {
    position: absolute;
    top: 34px;
    left: 0;
    width: 933px;
    margin: 0;
    text-align: center;
    font-family: "Archivo", Arial, sans-serif;
    font-weight: 800;
    text-transform: uppercase;
  }
  .brand-name {
    display: block;
    font-size: 26px;
    line-height: 29px;
    letter-spacing: 0.5px;
    color: var(--brand-red);
  }
  .brand-suffix {
    display: block;
    margin-top: 2px;
    font-size: 14px;
    line-height: 18px;
    letter-spacing: 0.4px;
    color: var(--brand-blue);
  }
  .footer-art {
    position: absolute;
    left: 0;
    top: 1140px;
    width: 933px;
    height: 60px;
  }
  .tagline {
    position: absolute;
    left: 118px;
    top: 1172px;
    margin: 0;
    font-family: "Lato", Arial, sans-serif;
    font-size: 4px;
    color: var(--brand-blue);
    letter-spacing: 2px;
  }
</style>
</head>
<body>
<main class="letterhead">
  <h1 class="brand-block">
    <span class="brand-name">Brindlecroft<br>Arcwell</span>
    <span class="brand-suffix">Incorporated</span>
  </h1>

  <svg class="footer-art" viewBox="0 0 933 60" aria-hidden="true">
    <rect x="105" y="42" width="735" height="3" fill="var(--brand-blue)"/>
    <polygon points="354,13 366,13 342,46 327,46" fill="var(--brand-blue)"/>
    <polygon points="366,13 577,13 605,46 342,46" fill="var(--brand-red)"/>
    <polygon points="580,13 592,13 620,46 605,46" fill="var(--brand-blue)"/>
    <rect x="0" y="49" width="933" height="11" fill="var(--brand-red)"/>
  </svg>

  <p class="tagline">lighting · sustainability · ahead</p>
</main>
</body>
</html>
```